Need a professional looking Consulting site for Consulting Services Company

Stock professional office images with a registration page for contact

Coding

Coded - Design and coding required

```html
<!DOCTYPE html>
<html lang="en">
<head>
<meta charset="utf-8">
<title>Verdexa — Consulting Services</title>
<link href="https://fonts.googleapis.com/css2?family=Poppins:wght@600;700&family=Roboto:wght@400;500;700&display=swap" rel="stylesheet">
<style>
:root{
  --green:#2f8f3a;
  --green-bright:#3aa845;
  --dark:#151515;
  --ink:#1b1b1b;
  --muted:#777;
  --white:#fff;
  --hero-a:#e9eaee;
  --hero-b:#b9c2cf;
}
*{box-sizing:border-box;margin:0;padding:0}
html,body{width:1200px;height:3478px;overflow:hidden}
body{position:relative;background:var(--white);font-family:'Roboto',sans-serif;color:var(--ink)}
.abs{position:absolute}
h1,h2,h3{font-family:'Poppins',sans-serif}
.accent{color:var(--green)}

/* header */
.logo{left:144px;top:22px;display:flex;flex-direction:column}
.logo-name{font-family:'Poppins',sans-serif;font-weight:600;font-size:40px;line-height:1.05;color:var(--green);display:flex;align-items:center;gap:10px}
.logo-dot{width:16px;height:16px;border-radius:50%;background:var(--green)}
.logo-tag{font-size:9px;font-weight:700;color:var(--ink);margin-left:26px;margin-top:1px}
.nav{left:448px;top:27px;width:608px;height:45px;background:var(--green);display:flex;align-items:center;z-index:3}
.nav a{color:var(--white);font-size:13px;font-weight:500;text-decoration:none;padding:0 14px}
.nav .home{background:var(--dark);height:45px;display:flex;align-items:center;padding:0 24px 0 48px;clip-path:polygon(28px 0,100% 0,100% 100%,0 100%)}
.nav .search{width:12px;height:12px;border:2px solid #fff;border-radius:50%;margin-left:14px;position:relative}
.nav .search::after{content:"";position:absolute;width:2px;height:6px;background:#fff;right:-4px;bottom:-5px;transform:rotate(-45deg)}

/* hero */
.hero-photo{left:0;top:0;width:1200px;height:760px;background:linear-gradient(100deg,var(--hero-a) 0%,#dfe2e8 40%,var(--hero-b) 75%,#8e9bb0 100%)}
.hero-curve{left:0;top:560px;width:1200px;height:200px}
.hero-title{left:140px;top:220px;font-size:80px;line-height:1;font-weight:700;letter-spacing:2px;color:var(--ink)}
.hero-sub{left:144px;top:320px;font-size:19px;color:#333}
.btn{display:flex;align-items:center;justify-content:center;border-radius:31px;color:#fff;font-size:17px;font-weight:500;text-decoration:none}
.btn-start{left:144px;top:382px;width:189px;height:61px;background:var(--green)}
.dots{left:144px;top:499px;display:flex;gap:7px}
.dots span{width:8px;height:8px;border-radius:50%;background:#c3c6cb}
.dots .on{background:var(--green)}

/* offer */
.section-title{width:1200px;left:0;text-align:center;font-size:46px;font-weight:700}
.offer-bg{left:0;top:1215px;width:1200px;height:560px;background:linear-gradient(180deg,rgba(255,255,255,1) 0%,rgba(170,200,225,.9) 20%,#7d93aa 55%,#546173 85%,var(--green) 100%)}
.card{width:445px;height:215px;background:#fff;box-shadow:0 10px 40px rgba(0,0,0,.12);display:flex;padding:8px}
.card-img{width:174px;height:199px;flex:none}
.card-body{padding:25px 0 0 34px}
.card-body h3{font-family:'Roboto',sans-serif;font-size:18px;font-weight:500;margin-bottom:18px}
.card-body p{font-size:12.5px;line-height:24px;color:var(--muted);width:220px}
.more{display:block;margin-top:14px;font-size:13px;font-weight:700;color:var(--green);text-decoration:none}

/* about */
.about{left:0;top:1755px;width:1200px;height:545px;background:var(--green)}
.about-title{left:144px;top:1838px;font-size:46px;color:#fff}
.about-text{left:144px;top:1921px;width:440px;font-size:13px;line-height:24px;color:#fff}
.btn-dark{left:144px;top:2132px;width:189px;height:61px;background:var(--dark)}
.about-art{left:628px;top:1748px;width:500px;height:500px;border-radius:50%;background:radial-gradient(circle,#5ee36a 0%,#34b244 50%,rgba(47,143,58,0) 72%)}

/* news */
.news{width:297px}
.news-img{width:297px;height:179px;position:relative}
.news-date{position:absolute;left:16px;bottom:-14px;width:111px;height:30px;background:var(--green);color:#fff;font-size:13px;font-weight:700;display:flex;align-items:center;justify-content:center}
.news h3{font-family:'Roboto',sans-serif;font-size:13px;font-weight:700;margin-top:42px}
.news p{font-size:11.5px;line-height:22px;color:#888;margin-top:8px}
.news .more{margin-top:12px}

/* contact */
.contact-bg{left:0;top:2900px;width:1200px;height:578px}
.contact-title{color:#fff;top:2998px}
.label{font-size:15px;font-weight:500;color:#fff}
.field{background:#fff;border:1px solid #999;font-size:10px;color:#555;padding:9px 10px}
.submit{left:632px;top:3313px;width:77px;height:28px;border-radius:14px;background:var(--green);color:#fff;font-size:11px;font-weight:500;display:flex;align-items:center;justify-content:center}
.info-row{left:780px;display:flex;align-items:center;gap:17px;color:#fff;font-size:11.5px;line-height:17px}
.info-icon{width:34px;height:34px;border:2px solid #fff;border-radius:50%;flex:none;display:flex;align-items:center;justify-content:center}
.footer-line{left:132px;top:3393px;width:936px;height:1px;background:#333}
.copy{left:144px;top:3426px;font-size:11.5px;color:#fff}
.social{left:890px;top:3421px;display:flex;gap:7px}
.social span{width:27px;height:27px;border-radius:50%}
</style>
</head>
<body>

<!-- hero -->
<div class="abs hero-photo" role="img" aria-label="Photo of two smiling business consultants reviewing a tablet at an office desk"></div>
<svg class="abs hero-curve" viewBox="0 0 1200 200" preserveAspectRatio="none" aria-hidden="true">
  <path d="M0 25 Q600 290 1200 25 L1200 200 L0 200 Z" fill="#fff"/>
  <path d="M0 25 Q600 290 1200 25" fill="none" stroke="#2f8f3a" stroke-width="9"/>
</svg>

<header>
  <div class="abs logo">
    <div class="logo-name"><span class="logo-dot"></span>Verdexa</div>
    <div class="logo-tag">Strategy &amp; Advisory for Growing Companies</div>
  </div>
  <nav class="abs nav">
    <a class="home" href="#">HOME</a>
    <a href="#">ABOUT</a>
    <a href="#">SERVICES</a>
    <a href="#">NEWS</a>
    <a href="#">REVIEWS</a>
    <a href="#">CONTACT</a>
    <span class="search"></span>
  </nav>
</header>

<h1 class="abs hero-title">VERDEXA</h1>
<p class="abs hero-sub">We are a Consulting Services Company</p>
<a class="abs btn btn-start" href="#">GET STARTED</a>
<div class="abs dots"><span></span><span class="on"></span><span></span><span></span></div>

<!-- offer -->
<div class="abs offer-bg" role="img" aria-label="Photo of hands using a tablet and laptop with business charts"></div>
<h2 class="abs section-title" style="top:826px">What <span class="accent">We Offer</span></h2>

<div class="abs card" style="left:144px;top:946px">
  <div class="card-img" style="background:linear-gradient(135deg,#c9c4bb,#7d7a76)" role="img" aria-label="Photo of a team working with laptops and documents"></div>
  <div class="card-body"><h3>Sed ut perspiciatis</h3><p>Lorem ipsum dolor sit amonsectetur adipiscing elied do eiusmod tempor incididunt ut labore et dolore</p><a class="more" href="#">READ MORE</a></div>
</div>
<div class="abs card" style="left:612px;top:946px">
  <div class="card-img" style="background:linear-gradient(135deg,#d8d8d4,#8c8e90)" role="img" aria-label="Photo of a businesswoman shaking hands in an office"></div>
  <div class="card-body"><h3>Nemo enim ipsa</h3><p>Lorem ipsum dolor sit amonsectetur adipiscing elied do eiusmod tempor incididunt ut labore et dolore</p><a class="more" href="#">READ MORE</a></div>
</div>
<div class="abs card" style="left:378px;top:1191px">
  <div class="card-img" style="background:linear-gradient(135deg,#d2d6dc,#5f7391)" role="img" aria-label="Photo of hands reviewing financial charts on a tablet"></div>
  <div class="card-body"><h3>Neque porro quisqu</h3><p>Lorem ipsum dolor sit amonsectetur adipiscing elied do eiusmod tempor incididunt ut labore et dolore</p><a class="more" href="#">READ MORE</a></div>
</div>

<!-- about -->
<section class="abs about"></section>
<h2 class="abs about-title">About Us</h2>
<p class="abs about-text">Lorem ipsum dolor sit amet, consectetur adipiscing elit, sed do eiusmod tempor incididunt ut labore et dolore magna aliqua.uis ipsum suspendisse ultrices gravidisus commodo viverra maecenas accumsan lacus vel facilisis. Lorem ipsum dolor sit amet, consectetur adipiscing elit, sed do eiusmod tempor incididunt ut labore et dolore magna aliquais ipsum suspendisse ultrices gravidus commodo viverra maecenas acdo eiusmod tempoi ncididunt ut labore et dolore magna aliquais ipsumus vel facilisis.</p>
<a class="abs btn btn-dark" href="#">READ MORE</a>
<div class="abs about-art" role="img" aria-label="Green leaf-shaped illustration with a smiling consultant inside"></div>

<!-- news -->
<h2 class="abs section-title" style="top:2388px">Latest <span class="accent">News</span></h2>
<article class="abs news" style="left:132px;top:2497px">
  <div class="news-img" style="background:linear-gradient(135deg,#c2c0bc,#4f5a6a)" role="img" aria-label="Photo of colleagues discussing documents in an office"><span class="news-date">31 JULY 2021</span></div>
  <h3>UM QUIA DOLOR SIT AMETONSECTE</h3>
  <p>Sed ut perspiciatis unde omnis iste natus error<br>sit voluptatem accusantium doloremque</p>
  <a class="more" href="#">READ MORE</a>
</article>
<article class="abs news" style="left:451px;top:2497px">
  <div class="news-img" style="background:linear-gradient(135deg,#dfe2e4,#7f8a8e)" role="img" aria-label="Photo of a bright open-plan office with people at work"><span class="news-date">31 JULY 2021</span></div>
  <h3>UM QUIA DOLOR SIT AMETONSECTE</h3>
  <p>Sed ut perspiciatis unde omnis iste natus error<br>sit voluptatem accusantium doloremque</p>
  <a class="more" href="#">READ MORE</a>
</article>
<article class="abs news" style="left:771px;top:2497px">
  <div class="news-img" style="background:linear-gradient(135deg,#e6e8ea,#8a96a3)" role="img" aria-label="Photo of hands reviewing charts on a laptop and tablet"><span class="news-date">31 JULY 2021</span></div>
  <h3>UM QUIA DOLOR SIT AMETONSECTE</h3>
  <p>Sed ut perspiciatis unde omnis iste natus error<br>sit voluptatem accusantium doloremque</p>
  <a class="more" href="#">READ MORE</a>
</article>

<!-- contact -->
<svg class="abs contact-bg" viewBox="0 0 1200 578" preserveAspectRatio="none" aria-hidden="true">
  <path d="M0 185 Q600 -160 1200 185 L1200 578 L0 578 Z" fill="#151515"/>
  <path d="M0 185 Q600 -160 1200 185" fill="none" stroke="#2f8f3a" stroke-width="9"/>
</svg>
<h2 class="abs section-title contact-title">Contact <span class="accent">Us</span></h2>

<div class="abs label" style="left:165px;top:3105px">Get In Touch:</div>
<form>
  <div class="abs field" style="left:167px;top:3147px;width:266px;height:29px">NAME :</div>
  <div class="abs field" style="left:444px;top:3147px;width:265px;height:29px">PHONE :</div>
  <div class="abs field" style="left:167px;top:3189px;width:542px;height:28px">EMAIL :</div>
  <div class="abs field" style="left:167px;top:3228px;width:542px;height:66px">MESSAGE :</div>
  <div class="abs submit">SUBMIT</div>
</form>

<div class="abs label" style="left:780px;top:3105px">Contact Information</div>
<div class="abs info-row" style="top:3147px">
  <span class="info-icon"><svg width="14" height="16" viewBox="0 0 14 18"><path d="M7 1a6 6 0 0 0-6 6c0 4.5 6 10 6 10s6-5.5 6-10a6 6 0 0 0-6-6z" fill="none" stroke="#fff" stroke-width="1.8"/><circle cx="7" cy="7" r="2" fill="#fff"/></svg></span>
  <span>12,Sed ut perspiciatis unde omnis iste<br>natus error sit voluptatem</span>
</div>
<div class="abs info-row" style="top:3196px">
  <span class="info-icon"><svg width="14" height="14" viewBox="0 0 16 16"><path d="M3 1l3 3-2 2c1 2 3 4 6 6l2-2 3 3-2 2C7 15 1 9 1 3z" fill="#fff"/></svg></span>
  <span>Phone : 1 888 888 8888</span>
</div>
<div class="abs info-row" style="top:3241px">
  <span class="info-icon"><svg width="14" height="11" viewBox="0 0 16 12"><rect x="0" y="0" width="16" height="12" rx="1.5" fill="#fff"/><path d="M1 1l7 6 7-6" fill="none" stroke="#151515" stroke-width="1.5"/></svg></span>
  <span>info@verdexa-mail.com</span>
</div>
<div class="abs info-row" style="top:3289px">
  <span class="info-icon"><svg width="14" height="14" viewBox="0 0 16 16"><circle cx="8" cy="8" r="6.5" fill="none" stroke="#fff" stroke-width="1.6"/><path d="M8 4v4h3" fill="none" stroke="#fff" stroke-width="1.6"/></svg></span>
  <span style="font-size:17px;font-weight:700">24/7</span>
</div>

<footer>
  <div class="abs footer-line"></div>
  <p class="abs copy">Copyrights © 2021 Verdexa. All Rights Reserved.&nbsp; |&nbsp; Privacy policy</p>
  <div class="abs social" aria-label="Social links">
    <span style="background:#3b5998"></span>
    <span style="background:#1da1f2"></span>
    <span style="background:#e52d27"></span>
    <span style="background:#b8894f"></span>
    <span style="background:#0e76a8"></span>
  </div>
</footer>

</body>
</html>
```